Organic lawn care

take the same sign as the mosquito sign, only instead of the mosquito image have the red circle and line cross out the text of "chemicals". Have the sign say "this lawn receives ORGANIC grass treatments" "instantly SAFE for people and pets"

Lawn Care

```html
<!DOCTYPE html>
<html lang="en">
<head>
<meta charset="utf-8">
<title>No Chemical Spraying – Lawn Sign</title>
<link rel="stylesheet" href="https://fonts.googleapis.com/css2?family=Montserrat:wght@600;700&family=Open+Sans:wght@400;600;700&display=swap">
<style>
  :root {
    --navy: #1f5f8f;
    --sky: #3d9ad5;
    --leaf: #8dc63f;
    --alert-red: #d7262e;
    --paper: #ffffff;
    --edge: #9a9a9a;
  }
  * { box-sizing: border-box; margin: 0; padding: 0; }
  html, body {
    width: 1200px;
    height: 799px;
    overflow: hidden;
    background: var(--paper);
  }
  .sign {
    position: relative;
    width: 1200px;
    height: 799px;
    background: var(--paper);
    border: 3px solid var(--edge);
    font-family: "Open Sans", Arial, sans-serif;
  }
  .headline {
    position: absolute;
    left: 20px;
    top: 58px;
    width: 620px;
    text-align: center;
    font-family: "Montserrat", Arial, sans-serif;
    font-weight: 700;
    font-size: 70px;
    line-height: 76px;
    color: var(--navy);
    letter-spacing: 1px;
  }
  .message {
    position: absolute;
    left: 20px;
    top: 262px;
    width: 620px;
    text-align: center;
    font-size: 44px;
    line-height: 58px;
    color: var(--sky);
  }
  .message .accent {
    color: var(--leaf);
    font-weight: 700;
    letter-spacing: 12px;
  }
  .ban-mark {
    position: absolute;
    left: 625px;
    top: 55px;
    width: 470px;
    height: 470px;
  }
  .ban-word {
    font-family: "Montserrat", Arial, sans-serif;
    font-weight: 700;
    font-size: 54px;
    letter-spacing: 1px;
    fill: var(--navy);
  }
  .website {
    position: absolute;
    left: 46px;
    top: 660px;
    display: flex;
    align-items: center;
    gap: 12px;
    font-size: 64px;
    line-height: 90px;
    color: var(--sky);
  }
  .website .dot {
    width: 20px;
    height: 20px;
    border-radius: 50%;
    background: var(--leaf);
  }
  .call {
    position: absolute;
    left: 610px;
    width: 530px;
    text-align center;
    text-align: center;
    font-family: "Montserrat", Arial, sans-serif;
    font-weight: 700;
    color: var(--navy);
  }
  .call-label {
    top: 606px;
    font-size: 46px;
    line-height: 56px;
    letter-spacing: 9px;
  }
  .call-number {
    top: 670px;
    font-size: 56px;
    line-height: 70px;
    letter-spacing: 3px;
  }
</style>
</head>
<body>
  <main class="sign">
    <h1 class="headline">NO CHEMICAL<br>SPRAYING</h1>

    <p class="message">
      This lawn receives<br>
      <span class="accent">ORGANIC</span><br>
      grass treatments.<br>
      Instantly <span class="accent">SAFE</span><br>
      for people and pets.
    </p>

    <svg class="ban-mark" viewBox="0 0 470 470" role="img" aria-label="Chemicals crossed out">
      <text class="ban-word" x="235" y="254" text-anchor="middle">CHEMICALS</text>
      <circle cx="235" cy="235" r="212" fill="none" stroke="var(--alert-red)" stroke-width="30"></circle>
      <line x1="85" y1="85" x2="385" y2="385" stroke="var(--alert-red)" stroke-width="30"></line>
    </svg>

    <div class="website"><span class="name">lawnleaf.com</span><span class="dot"></span></div>

    <p class="call call-label">CALL</p>
    <p class="call call-number">615-555-0147</p>
  </main>
</body>
</html>
```